Broschüre für Beratungsunternehmen für Führungskräfte
Zielgruppe
Wir sind ein Beratungsunternehmen für Führungskräfte und Organisationen, Wir bieten Prozessberatung, Einzelcoachings, Workshops und zukünftig begleitende Online-Inhalte wie Online-Videokurs
Aufgabenstellung
Es gilt ein Workbook, dass einen Online-Videokurs begleitet zu gestalten. Wir haben eine CI (siehe www.lvmerkhaus.de) was Logo und Farbgebung (blau, schwarz, weiß) betrifft. In diesem Stil sollte das Workbook gehalten sein. Es sollte eher schlicht sein und nicht verspielt, aber stilvoll wirken.
Das Workbook soll als PDF zur Verfügung stehen, da es in der Regel als Download verbreitet werden wird.

```html
<!DOCTYPE html>
<html lang="de">
<head>
<meta charset="utf-8">
<title>Workbook Work-Life-Design</title>
<link rel="stylesheet" href="https://fonts.googleapis.com/css2?family=Open+Sans:wght@400;600;700&family=Arimo:wght@400;700&display=swap">
<style>
  :root {
    --board: #e9e9e9;
    --paper: #ffffff;
    --brand-blue: #1f5aa8;
    --ink: #1a1a1a;
    --text: #3c3c3c;
    --muted: #6a6a6a;
    --rule: #dcdcdc;
    --field: #ebebeb;
    --footer: #b5b5b5;
  }
  * { margin: 0; padding: 0; box-sizing: border-box; }
  html, body { width: 701px; height: 1200px; overflow: hidden; }
  body {
    position: relative;
    background: radial-gradient(ellipse at 50% 40%, #f1f1f1 0%, var(--board) 70%);
    font-family: "Open Sans", Arial, sans-serif;
    color: var(--text);
  }

  /* Presentation label */
  .board-brand { position: absolute; left: 37px; top: 44px; }
  .board-brand__mark {
    font-family: "Open Sans", Arial, sans-serif;
    font-weight: 400; font-size: 30px; color: var(--ink);
    letter-spacing: 0.5px; line-height: 1;
  }
  .board-label { position: absolute; left: 37px; top: 109px; font-family: "Arimo", Arial, sans-serif; color: var(--muted); }
  .board-label__company { font-size: 11.6px; font-weight: 700; line-height: 16px; }
  .board-label__version { font-size: 11.6px; font-weight: 400; line-height: 18px; }

  /* Pages */
  .page {
    position: absolute; width: 217px; height: 307px;
    background: var(--paper);
    box-shadow: 0 1px 6px rgba(0,0,0,0.10);
    overflow: hidden;
  }
  .page--cover { left: 374px; top: 45px; }
  .page--p2 { left: 100px; top: 406px; }
  .page--p3 { left: 375px; top: 406px; }
  .page--p4 { left: 100px; top: 762px; }
  .page--p6 { left: 375px; top: 762px; }

  /* Cover */
  .cover__brand {
    position: absolute; top: 68px; left: 0; width: 100%; text-align: center;
    font-size: 17px; font-weight: 400; color: var(--ink); line-height: 1;
  }
  .cover__photo {
    position: absolute; left: 0; top: 72px; width: 100%; height: 122px;
    background:
      radial-gradient(ellipse at 78% 55%, #fff6e4 0%, rgba(255,240,215,0) 55%),
      linear-gradient(200deg, #f3d7b8 0%, #eab98a 40%, #e2a676 62%, #d99464 100%);
  }
  .cover__eyebrow { position: absolute; left: 31px; top: 220px; font-size: 7px; color: var(--brand-blue); font-weight: 600; }
  .cover__title {
    position: absolute; left: 31px; top: 230px;
    font-size: 13px; line-height: 14.5px; font-weight: 700; color: var(--brand-blue);
  }

  /* Page furniture */
  .page__header {
    position: absolute; left: 31px; right: 31px; top: 16px; height: 9px;
    border-bottom: 0.5px solid var(--rule);
    font-size: 3.8px; text-align: right; color: var(--text); letter-spacing: 0.1px;
  }
  .page__footer {
    position: absolute; left: 31px; right: 31px; top: 282px;
    border-top: 0.5px solid var(--rule); padding-top: 1.3px;
    display: flex; justify-content: space-between; align-items: flex-start;
  }
  .page__legal { font-size: 1.6px; line-height: 2.2px; color: var(--footer); }
  .page__number { font-size: 3.6px; color: var(--text); padding-top: 3px; }

  .page__body {
    position: absolute; left: 31px; right: 31px;
    font-size: 3.55px; line-height: 5.85px; text-align: justify; hyphens: auto;
  }
  .page__body p { margin-bottom: 5.85px; }
  .page__body strong { font-weight: 700; color: var(--ink); }

  .lead { font-size: 4.3px; line-height: 6px; color: var(--text); margin-bottom: 1px; }
  .chapter-title { font-size: 8.4px; line-height: 11.6px; font-weight: 600; color: var(--brand-blue); letter-spacing: 0.15px; text-align: left; }
  .section-title { font-size: 4.3px; line-height: 6px; font-weight: 700; color: var(--brand-blue); margin: 2px 0 5.5px; text-align: left; }

  .strategy-list { list-style: none; margin: 0 0 5.85px 3px; }
  .strategy-list li { margin-bottom: 5.85px; text-align: left; }
  .strategy-list b { font-weight: 700; color: var(--ink); }
  .strategy-list span { display: block; padding-left: 5px; }

  .exercise__prompt { position: absolute; left: 31px; right: 31px; font-size: 3.55px; line-height: 5.85px; }
  .exercise__field { position: absolute; left: 31px; right: 31px; background: var(--field); }
</style>
</head>
<body>

  <div class="board-brand"><span class="board-brand__mark">NBK</span></div>
  <div class="board-label">
    <div class="board-label__company">Nordhafen Beratungskontor</div>
    <div class="board-label__version">Workbook A4 - Version 1</div>
  </div>

  <!-- Cover -->
  <section class="page page--cover">
    <div class="cover__brand" style="top:31px">NBK</div>
    <div class="cover__photo" role="img" aria-label="Foto: Segelyacht in Schräglage auf dem Meer im warmen Gegenlicht der Sonne"></div>
    <div class="cover__eyebrow">Workbook</div>
    <h1 class="cover__title">Work-Life-Design<br>Die Job-Crafting Methode</h1>
  </section>

  <!-- Page 2 -->
  <section class="page page--p2">
    <div class="page__header">www.lvmerkhaus.de</div>
    <div class="page__body" style="top:50px">
      <p class="lead" style="margin-bottom:1px">Toll, dass du dabei bist. Eine gute Entscheidung!</p>
      <h2 class="chapter-title" style="margin-bottom:13px">Was ist Job Crafting eigentlich?<br>Was es nicht ist:</h2>
      <p>Es geht dabei nicht so sehr darum andere Menschen zu motivieren – im Übrigen glaube ich, dass Motivation von außen („extrinsisch“) durch Belohnungen ohnehin nicht funktioniert – und die Forschung bestätigt das übrigens: In der Psychologie nennen wir dies „Overjustification“, also Überrechtfertigung. Wenn jemand eine Tätigkeit von sich aus gern ausführt und man nun beginnt ihn dafür zu belohnen, passiert Folgendes, sobald die Belohnungen ausgesetzt werden: Das Verhalten bleibt aus – die Motivation ist dann also ganz weg.</p>
      <p>Bei Job Crafting geht es darum den eigenen Job aus einer Selbstverantwortung heraus proaktiv mit Freude auf eine Weise zu gestalten, dass es leichter fällt, die eigene Person als Ganzes mit allen Stärken, Potenzialen und Zielen einbringen zu können. In diesem Workbook beginnen wir mit einer Gegenstandsbestimmung: Was ist Job Design und Job Crafting. Wir greifen ein tolles Beispiel auf, um das Prinzip zu illustrieren und besprechen, welche grundsätzliche Einstellung die Voraussetzung für Job Crafting ist, welches Mindset du brauchst.</p>
      <p>Damit du dein Ziel erreichen kannst, die Passung zwischen deiner Person und deinem Job zu verbessern, beleuchten wir zunächst Aspekte deiner Person, die du idealerweise mit deinem Job verbinden kannst. Wir erkunden dazu deine Stärken, deine Motive und prüfen, wofür du bei der Arbeit eigentlich „angetreten“ bist (das „Warum?“, deinen Sinn). Außerdem erkunden wir, bei welchen Aufgaben du leichter in den „Flow“ kommst. Dann beginnen wir mit der Job-Crafting Übung, die sich in das „Vorher-Bild“ und das „Nachher-Bild“ unterteilt. Am Ende gehen wir in die Umsetzungsplanung und ziehen ein Fazit, damit du größtmöglichen Nutzen für deine Zukunft erzielst und persönlichen Erfolg und Wachstum erfährst.</p>
      <p><strong>Auf geht’s!</strong></p>
    </div>
    <div class="page__footer">
      <div class="page__legal">Copyright: NBK Nordhafen Beratungskontor GmbH<br>Vervielfältigung und Weitergabe nur mit schriftlicher Genehmigung</div>
      <div class="page__number">2</div>
    </div>
  </section>

  <!-- Page 3 -->
  <section class="page page--p3">
    <div class="page__header">www.lvmerkhaus.de</div>
    <div class="page__body" style="top:47px">
      <h2 class="chapter-title" style="margin-bottom:13px">Definition:<br>Job-Design und Job-Crafting</h2>
      <p>In diesem Kapitel besprechen wir, was Job-Crafting ist und welche Bedeutung es für dein Berufsleben haben kann. In der Regel beginnt alles mit dem Job-Design. Also der Stellenbeschreibung oder Aufgabenbeschreibung, die du zu Beginn einmal von deinem Chef oder einem Personalmitarbeiter erhalten oder in der Stellenausschreibung gelesen hast. Dieses Job-Design wird also von „oben“ vorgegeben und beinhaltet in der Regel eine Liste von Aufgaben oder Aufgabenkategorien, die dieser Tätigkeit zugeordnet sind. Zusätzlich sind bestimmte Beziehungen zu anderen Kollegen vorgegeben und Schnittstellen innerhalb des Unternehmens benannt. Die Stelle ist in der Organisation „aufgehängt“, also im Organigramm verortet.</p>
      <p>Hier kann bereits vieles richtig oder eben leider auch falsch laufen, wenn es um gute Voraussetzungen für eine erfüllende Tätigkeit geht.</p>
      <p>Die Kernmerkmale des Job-Designs, die einen massiven Einfluss darauf haben, wie zufrieden der einzelne Mitarbeiter in einer Position ist, wurden von Hartmann und Olsen im sogenannten Job Characteristics Modell beschrieben. Wenn diese Faktoren erfüllt sind, dann, so haben Studien gezeigt, sind die Stelleninhaber zufriedener, motivierter, erleben einen Sinn, eine Bedeutung in ihrer Arbeit. Außerdem gehen Fehlzeiten und Fluktuation zurück. Alles Dinge die Unternehmen heute viel Geld kosten und bei dem einzelnen Arbeitnehmer zu Lasten der Gesundheit und Lebensenergie gehen. Aktuelle Fehlzeitenreports bestätigen dies immer wieder.</p>
      <h3 class="section-title">Die Kernmerkmale des JCM</h3>
      <p>Zunächst einmal ist die Vielseitigkeit der Aufgaben von Bedeutung. Wenn ich immer wieder eine gleichförmige Tätigkeit am Fließband ausführen muss (etwa das Festziehen der immer gleichen Schraube), dann geht dies nachvollziehbarerweise auf Kosten der Motivation. Außerdem ist die Aufgabenidentität, die Ganzheitlichkeit der Aufgabe, wichtig: Drehe ich nur an einem Bauteil, oder fertige ich nach und nach ein ganzes Auto? Die Aufgabenbedeutung ist der dritte Faktor. Eine kleine Schraube verändert vielleicht nicht viel, aber wenn ich sehe, wie ein Kunde von der Tätigkeit profitiert oder sich über das Auto, dass ich gebaut habe freut, dann wirkt sich dies positiv aus.</p>
    </div>
    <div class="page__footer">
      <div class="page__legal">Copyright: NBK Nordhafen Beratungskontor GmbH<br>Vervielfältigung und Weitergabe nur mit schriftlicher Genehmigung</div>
      <div class="page__number">3</div>
    </div>
  </section>

  <!-- Page 4 -->
  <section class="page page--p4">
    <div class="page__header">www.lvmerkhaus.de</div>
    <div class="page__body" style="top:40px">
      <p>Der vierte Faktor ist die Autonomie. Damit ist die Freiwilligkeit der Aufgabe und der Entscheidungsspielraum gemeint. Kann ich meine Tätigkeit, die Teilaufgaben selbstständig strukturieren, priorisieren und verändern? Ich kann dabei auch, wenn ich nur Anweisungen ausführe freiwillig handeln, wenn ich mich mit dem Nutzen der ausführenden Tätigkeit identifiziere. Der fünfte wichtige Aspekt, der sich auf die Zufriedenheit auswirkt, ist das Ausmaß an Rückmeldung und Feedback. Erfahre ich, ob meine Leistungen gut oder schlecht sind?</p>
      <p>Mit diesen fünf Faktoren können beim Job-Design bereits die Weichen für zufriedene Arbeitnehmer gestellt werden.</p>
      <h3 class="section-title">Job-Crafting</h3>
      <p>Beim Job-Crafting versuche ich nun eigenverantwortlich als einzelner Mitarbeiter, die teilweise engen Grenzen meiner Stellenbeschreibung zu lockern, damit die Aufgaben und die Art sie zu erledigen besser zu mir passen. Dabei gibt es grundsätzlich drei Strategien im Job-Crafting:</p>
      <ol class="strategy-list">
        <li><b>1. &nbsp;Aufgabenbearbeitung „Task Crafting“</b><span>Auswahl bestimmter Aufgaben, mit denen ich meine Zeit verbringe</span></li>
        <li><b>2. &nbsp;Beziehungsgestaltung „Relational Crafting“</b><span>Auswahl und Fokussierung: Mit wem arbeite ich wie zusammen?</span></li>
        <li><b>3. &nbsp;Bedeutungsgebung „Cognitive Crafting“</b><span>Welchen Sinn sehe ich in meiner Tätigkeit? (Bin ich nur Putzmann im Krankenhaus „trage ich zu einem Umfeld bei, in dem Menschen optimal gesund werden können?“)</span></li>
      </ol>
      <p>In einem späteren Kapitel gehen wir auf diese Strategien noch im Detail ein. In der Regel ergibt sich eine Kombination der verschiedenen Strategien.</p>
      <h3 class="section-title">Warum betreiben wir Job-Crafting und welchen Nutzen hat dies?</h3>
      <p>Erstmal bleibt festzuhalten, dass die meisten von uns bereits erfahrene Job-Crafter sein dürften. Wir alle drücken uns mal um langweilige oder nervige Aufgaben, meiden bestimmte Kollegen oder bevorzugen die Zusammenarbeit mit anderen. Wie kann ich aber Job-Crafting auf eine besonders förderliche und zielgerichtete Art und Weise betreiben? Warum sollte ich das tun?</p>
    </div>
    <div class="page__footer">
      <div class="page__legal">Copyright: NBK Nordhafen Beratungskontor GmbH<br>Vervielfältigung und Weitergabe nur mit schriftlicher Genehmigung</div>
      <div class="page__number">4</div>
    </div>
  </section>

  <!-- Page 6 -->
  <section class="page page--p6">
    <div class="page__header">www.lvmerkhaus.de</div>
    <p class="exercise__prompt" style="top:40px">Welche Umsetzungswege für Task Crafting fallen dir ein? Welche Schlüsselerkenntnisse und Anregungen ziehst du aus diesem Abschnitt für deine Arbeit?</p>
    <div class="exercise__field" style="top:55px;height:52px"></div>
    <p class="exercise__prompt" style="top:122px">Welche Umsetzungswege für Relational Crafting fallen dir ein? Welche Schlüsselerkenntnisse und Anregungen ziehst du aus diesem Abschnitt für deine Arbeit?</p>
    <div class="exercise__field" style="top:137px;height:52px"></div>
    <p class="exercise__prompt" style="top:204px">Welche Umsetzungswege für Cognitive Crafting fallen dir ein? Welche Schlüsselerkenntnisse und Anregungen ziehst du aus diesem Abschnitt für deine Arbeit?</p>
    <div class="exercise__field" style="top:218px;height:53px"></div>
    <div class="page__footer">
      <div class="page__legal">Copyright: NBK Nordhafen Beratungskontor GmbH<br>Vervielfältigung und Weitergabe nur mit schriftlicher Genehmigung</div>
      <div class="page__number">6</div>
    </div>
  </section>

</body>
</html>
```